Need UI design for an iOS app game with most of the layout planned

The name of the game is "QUADRIX".

The goal of the game is to find a way to manipulate four numbers so that the end result is 24. Addition, subtraction, multiplication and division may be used and each number can only be used once.

The list of items we need is:

1. launch image, app icon, UI design of all scenes (10-12 scenes) of the app.
2. App background image should support screen size of both 640x1136.
3. Files are preferred to be in (.eps) format so that resolution can be adjusted later. But other file formats are welcome as long as resolution is high enough.
4. Icons, buttons, background image etc. should have their own file so that later they can be moved around in case design is changed.

The detailed requirement is in the attached file. The actual layout can vary if it can help achieve better result. We also attached several screenshots from iOS game "Glimtor". You can use that as your reference.

```html
<!DOCTYPE html>
<html lang="en">
<head>
<meta charset="utf-8">
<title>QUADRIX – Level Complete</title>
<link rel="stylesheet" href="https://fonts.googleapis.com/css2?family=Arimo:wght@400;700&display=swap">
<style>
  :root {
    --sky-light: #7fd0fb;
    --sky-mid: #2f9be8;
    --sky-deep: #1a6fd0;
    --grid-line: rgba(255,255,255,0.07);
    --navy: #0d4fa6;
    --navy-dark: #083c86;
    --orange: #ff9a12;
    --orange-light: #ffc24a;
    --orange-dark: #e67800;
    --orange-edge: #b85e00;
    --magenta: #d94de0;
    --magenta-dark: #8a2fa8;
    --white: #ffffff;
    --score-ink: #0f4a8e;
    --gold: #f4b234;
    --gold-dark: #a06a10;
    --silver: #f2f2f2;
    --silver-dark: #8a8a8a;
    --logo-ink: #ffa31a;
  }
  * { box-sizing: border-box; margin: 0; padding: 0; }
  html, body { width: 676px; height: 1200px; overflow: hidden; }
  body { font-family: "Arimo", Arial, sans-serif; }

  .screen {
    position: relative;
    width: 676px; height: 1200px; overflow: hidden;
    background:
      repeating-linear-gradient(0deg, var(--grid-line) 0 2px, transparent 2px 14px),
      repeating-linear-gradient(90deg, var(--grid-line) 0 2px, transparent 2px 14px),
      radial-gradient(ellipse 60% 45% at 50% 62%, var(--sky-light), var(--sky-mid) 60%, var(--sky-deep));
  }

  .corner-button {
    position: absolute; top: -2px; width: 130px; height: 130px; border-radius: 50%;
    background: radial-gradient(circle at 50% 35%, #2a86e0, var(--navy-dark));
    box-shadow: 0 4px 8px rgba(0,0,0,0.35);
    display: flex; align-items: center; justify-content: center;
  }
  .corner-button--settings { left: -33px; padding-left: 30px; padding-bottom: 4px; }
  .corner-button--store { right: -33px; padding-right: 30px; padding-bottom: 4px; }

  .brand-name {
    position: absolute; top: 36px; left: 0; width: 676px; text-align: center;
    font-weight: 700; font-size: 62px; letter-spacing: 1px; color: var(--logo-ink);
  }

  .level-banner {
    position: absolute; left: 76px; top: 195px; width: 528px; height: 130px;
    background: linear-gradient(90deg, var(--magenta), #b13fc8 50%, var(--magenta-dark));
    box-shadow: 0 3px 6px rgba(0,0,0,0.3);
  }
  .level-banner__pill {
    position: absolute; left: 33px; top: 6px; width: 466px; height: 118px; border-radius: 50%;
    background: radial-gradient(ellipse at 50% 30%, #1f7fe0, var(--navy-dark));
    border: 5px solid #d9e4ee;
    display: flex; align-items: center; justify-content: center;
    color: var(--white); font-size: 37px;
  }

  .tile {
    position: absolute;
    background: linear-gradient(180deg, var(--orange) 0%, var(--orange-dark) 100%);
    border: 2px solid var(--orange-edge);
    border-radius: 4px 4px 8px 8px;
    box-shadow: 0 3px 5px rgba(0,0,0,0.3);
    display: flex; align-items: center; justify-content: center;
    color: var(--white);
  }
  .tile::before {
    content: ""; position: absolute; left: 6px; right: 6px; top: -2px; height: 14px;
    background: linear-gradient(180deg, var(--orange-light), var(--orange));
    border-bottom: 2px solid var(--orange-edge);
    clip-path: polygon(3% 0, 97% 0, 100% 100%, 0 100%);
  }
  .tile > * { position: relative; margin-top: 12px; }

  .star-slot { top: 368px; width: 186px; height: 121px; }
  .star-slot--1 { left: 32px; }
  .star-slot--2 { left: 244px; }
  .star-slot--3 { left: 457px; }

  .score-box {
    position: absolute; left: 181px; top: 597px; width: 316px; height: 84px;
    background: #3f9ae3; border: 2px solid #2370c2;
    box-shadow: inset 0 0 14px rgba(0,40,100,0.55);
    display: flex; align-items: center; justify-content: center;
    font-size: 50px; color: var(--score-ink);
  }

  .reward-burst { position: absolute; left: 31px; top: 755px; width: 428px; height: 180px; }
  .reward-burst__label {
    position: absolute; inset: 0; display: flex; align-items: center; justify-content: center;
    color: var(--white); font-size: 46px; padding-right: 6px;
  }

  .coin-tile { left: 510px; top: 803px; width: 134px; height: 107px; }

  .nav-tile { top: 1030px; height: 121px; }
  .nav-tile--exit { left: 32px; width: 156px; }
  .nav-tile--next { left: 236px; width: 197px; font-size: 42px; font-weight: 700; }
  .nav-tile--replay { left: 486px; width: 157px; }
</style>
</head>
<body>
<main class="screen">
  <div class="corner-button corner-button--settings" aria-label="Settings">
    <svg width="54" height="54" viewBox="-27 -27 54 54" aria-hidden="true">
      <g fill="#fff">
        <circle r="17"/>
        <rect x="-5" y="-26" width="10" height="12" rx="1"/>
        <rect x="-5" y="-26" width="10" height="12" rx="1" transform="rotate(45)"/>
        <rect x="-5" y="-26" width="10" height="12" rx="1" transform="rotate(90)"/>
        <rect x="-5" y="-26" width="10" height="12" rx="1" transform="rotate(135)"/>
        <rect x="-5" y="-26" width="10" height="12" rx="1" transform="rotate(180)"/>
        <rect x="-5" y="-26" width="10" height="12" rx="1" transform="rotate(225)"/>
        <rect x="-5" y="-26" width="10" height="12" rx="1" transform="rotate(270)"/>
        <rect x="-5" y="-26" width="10" height="12" rx="1" transform="rotate(315)"/>
      </g>
      <circle r="7" fill="#0d4fa6"/>
    </svg>
  </div>

  <div class="brand-name">QUADRIX</div>

  <div class="corner-button corner-button--store" aria-label="Store">
    <svg width="70" height="70" viewBox="0 0 70 70" aria-hidden="true">
      <circle cx="35" cy="35" r="30" fill="none" stroke="#fff" stroke-width="5"/>
      <text x="35" y="48" text-anchor="middle" font-family="Arimo, sans-serif" font-size="38" font-weight="700" fill="#fff">$</text>
    </svg>
  </div>

  <section class="level-banner">
    <div class="level-banner__pill">Level 1 Completed</div>
  </section>

  <svg width="0" height="0" style="position:absolute">
    <defs>
      <polygon id="star-shape" points="0,-25 7.3,-9.6 24,-7.7 11.6,3.7 14.7,20.2 0,12 -14.7,20.2 -11.6,3.7 -24,-7.7 -7.3,-9.6"/>
    </defs>
  </svg>

  <div class="tile star-slot star-slot--1" aria-label="Three gold stars">
    <svg width="170" height="60" viewBox="0 0 170 60" aria-hidden="true">
      <g fill="var(--gold)" stroke="var(--gold-dark)" stroke-width="2">
        <use href="#star-shape" x="30" y="32"/>
        <use href="#star-shape" x="85" y="32"/>
        <use href="#star-shape" x="140" y="32"/>
      </g>
    </svg>
  </div>
  <div class="tile star-slot star-slot--2" aria-label="Three silver stars">
    <svg width="170" height="60" viewBox="0 0 170 60" aria-hidden="true">
      <g fill="var(--silver)" stroke="var(--silver-dark)" stroke-width="2">
        <use href="#star-shape" x="30" y="32"/>
        <use href="#star-shape" x="85" y="32"/>
        <use href="#star-shape" x="140" y="32"/>
      </g>
    </svg>
  </div>
  <div class="tile star-slot star-slot--3" aria-label="Empty star slot"></div>

  <div class="score-box">1000</div>

  <div class="reward-burst">
    <svg width="428" height="180" viewBox="-214 -90 428 180" aria-hidden="true">
      <defs>
        <radialGradient id="burst-fill" cx="50%" cy="40%" r="60%">
          <stop offset="0" stop-color="#2b8ae6"/>
          <stop offset="1" stop-color="#0a4aa2"/>
        </radialGradient>
      </defs>
      <polygon fill="url(#burst-fill)" stroke="#9aa3ad" stroke-width="4"
        points="212,0 183.8,10.9 201.5,27.5 165.7,31.8 171.5,52.4 131.5,49.5 124.6,72 84.4,62.4 65.5,84.8 29,69.2 0,88 -29,69.2 -65.5,84.8 -84.4,62.4 -124.6,72 -131.5,49.5 -171.5,52.4 -165.7,31.8 -201.5,27.5 -183.8,10.9 -212,0 -183.8,-10.9 -201.5,-27.5 -165.7,-31.8 -171.5,-52.4 -131.5,-49.5 -124.6,-72 -84.4,-62.4 -65.5,-84.8 -29,-69.2 0,-88 29,-69.2 65.5,-84.8 84.4,-62.4 124.6,-72 131.5,-49.5 171.5,-52.4 165.7,-31.8 201.5,-27.5 183.8,-10.9"/>
    </svg>
    <div class="reward-burst__label">Reward 10</div>
  </div>

  <div class="tile coin-tile" aria-label="Collect coins">
    <svg width="70" height="70" viewBox="0 0 70 70" aria-hidden="true">
      <circle cx="35" cy="35" r="29" fill="none" stroke="#fff" stroke-width="5"/>
      <text x="35" y="48" text-anchor="middle" font-family="Arimo, sans-serif" font-size="38" font-weight="700" fill="#fff">$</text>
    </svg>
  </div>

  <div class="tile nav-tile nav-tile--exit" aria-label="Exit">
    <svg width="80" height="66" viewBox="0 0 80 66" aria-hidden="true">
      <path d="M36 6 H8 V60 H36" fill="none" stroke="#fff" stroke-width="8" stroke-linejoin="round"/>
      <path d="M22 27 H52 V14 L76 33 L52 52 V39 H22 Z" fill="#fff"/>
    </svg>
  </div>
  <div class="tile nav-tile nav-tile--next"><span>NEXT</span></div>
  <div class="tile nav-tile nav-tile--replay" aria-label="Replay">
    <svg width="70" height="70" viewBox="0 0 70 70" aria-hidden="true">
      <path d="M24 13 A26 26 0 1 0 46 13" fill="none" stroke="#fff" stroke-width="9"/>
      <path d="M36 4 L58 10 L44 28 Z" fill="#fff"/>
    </svg>
  </div>
</main>
</body>
</html>
```